Criminal Defense Law Firm needs Stationary design Theme for a Business Card, Envelope, and Letterhea

Our Law Firm is seeking a general design concept for a business card, letterhead, and Envelope.

Our website is WillowcrestTrialDesk.com

A design for these three items is requested to keep branding in place for the firm. Would like to keep the Firm Colors on the website consistent with our branding on business cards, letterheads, and mailing envelopes #10 size to be exact.

We would like business cards printed front and back with Law firm Colors from website.

Letterhead with law firm colors as well. Design is not limited to just the header, but the footer can be utilized as well for email, website, phone, fax, etc.

Simple #10 envelope consisting of the same design principles set out in the previous two designs.

```html
<!DOCTYPE html>
<html lang="en">
<head>
<meta charset="utf-8">
<title>Willowcrest Trial Desk – Stationery</title>
<link rel="stylesheet" href="https://fonts.googleapis.com/css2?family=EB+Garamond:wght@500&family=Exo+2:wght@700&family=Open+Sans:wght@400;600&display=swap">
<style>
:root{
  --canvas:#6b6b6b;
  --paper:#ffffff;
  --gold:#a08c5f;
  --ink:#1f1212;
  --faint:#f1ede4;
  --faint-dark:#3a2e2e;
  --text:#2b2b2b;
}
*{margin:0;padding:0;box-sizing:border-box}
html,body{width:1200px;height:1000px;overflow:hidden;background:var(--canvas)}
body{position:relative;font-family:"Open Sans",Arial,sans-serif;color:var(--text)}
.sheet{position:absolute;background:var(--paper);overflow:hidden}
.sheet.dark{background:var(--ink)}
.wave{position:absolute;left:0;width:100%;display:block}
.wave.top{top:0}
.wave.bottom{bottom:0}
.brand{position:absolute;display:flex;align-items:center;gap:6px}
.brand-dot{border:1.5px solid var(--ink);border-radius:50%;flex:none}
.brand-name{font-family:"EB Garamond",Georgia,serif;font-weight:500;color:var(--ink);text-transform:uppercase;line-height:1.05;letter-spacing:.02em}
.dark .brand-dot{border-color:#fff}
.dark .brand-name{color:#fff}
.watermark{position:absolute;border:3px solid var(--faint);border-radius:50%}
.dark .watermark{border-color:var(--faint-dark)}
.footer-rule{position:absolute;left:0;width:100%;height:2px;background:var(--ink)}
.footer-rule.gold{height:3px;background:var(--gold)}
.contacts{position:absolute;list-style:none;font-size:5px;line-height:7px;color:var(--text)}
.contacts li{display:flex;align-items:center;gap:3px;white-space:nowrap}
.contacts li::before{content:"";width:5px;height:5px;border-radius:1px;background:var(--ink);flex:none}
.signer{position:absolute;font-size:6px;line-height:7px;color:var(--gold);text-align:right}
.signer small{display:block;font-size:4px;color:var(--text)}
.card-name{position:absolute;font-family:"Exo 2",Arial,sans-serif;font-weight:700;font-size:15px;color:var(--gold);letter-spacing:.04em}
.dark .card-name{color:#fff}
.card-role{position:absolute;font-size:8px;color:var(--text)}
.dark .card-role{color:#ddd}
.card-contacts{position:absolute;list-style:none;font-size:8.5px;line-height:11px;color:var(--text)}
.card-contacts li{display:flex;align-items:center;gap:5px}
.card-contacts li::before{content:"";width:7px;height:7px;border-radius:1.5px;background:var(--gold);flex:none}
.dark .card-contacts{color:#fff}
.dark .card-contacts li::before{background:#fff}
.options{position:absolute;left:478px;top:640px;color:#fff;font-size:16.5px;line-height:23px}
.flap{position:absolute;left:0;top:0;width:100%;height:55px;background:var(--gold);border-radius:0 0 18px 18px;display:flex;justify-content:center;align-items:center}
.flap-dot{width:30px;height:30px;border:1.5px solid #fff;border-radius:50%}
</style>
</head>
<body>

<!-- Letterhead option A -->
<section class="sheet letterhead" style="left:28px;top:20px;width:370px;height:522px">
  <svg class="wave top" viewBox="0 0 370 40" height="40" preserveAspectRatio="none">
    <path d="M0 0H370V22C300 30 230 8 150 12C90 15 40 20 0 16Z" fill="var(--gold)"/>
    <path d="M0 18C40 22 90 17 150 14C230 10 300 32 370 24C300 36 230 16 150 20C90 24 40 30 0 28Z" fill="var(--ink)"/>
  </svg>
  <div class="brand" style="left:24px;top:40px"><span class="brand-dot" style="width:22px;height:22px"></span><span class="brand-name" style="font-size:10px">Willowcrest Trial<br>Desk</span></div>
  <div class="watermark" style="left:98px;top:208px;width:172px;height:172px"></div>
  <div class="signer" style="left:24px;top:498px">Peter Lund<small>Attorney</small></div>
  <ul class="contacts" style="left:76px;top:496px"><li>0555.014.2290</li><li>office@willowcrest.com</li></ul>
  <ul class="contacts" style="left:136px;top:496px"><li>web@willowcrest.com</li><li>12 Orchard Lane, Fairhaven, NM 87001</li></ul>
  <div class="footer-rule" style="bottom:5px"></div>
  <div class="footer-rule gold" style="bottom:0"></div>
</section>

<!-- Letterhead option B -->
<section class="sheet letterhead" style="left:428px;top:20px;width:370px;height:522px">
  <svg class="wave top" viewBox="0 0 370 40" height="40" preserveAspectRatio="none">
    <path d="M0 0H370V22C300 30 230 8 150 12C90 15 40 20 0 16Z" fill="var(--gold)"/>
    <path d="M0 18C40 22 90 17 150 14C230 10 300 32 370 24C300 36 230 16 150 20C90 24 40 30 0 28Z" fill="var(--ink)"/>
  </svg>
  <div class="brand" style="left:24px;top:40px"><span class="brand-dot" style="width:22px;height:22px"></span><span class="brand-name" style="font-size:10px">Willowcrest Trial<br>Desk</span></div>
  <div class="signer" style="left:218px;top:54px">Peter Lund<small>Attorney</small></div>
  <ul class="contacts" style="left:268px;top:46px;border-left:1px solid var(--ink);padding-left:4px"><li>0555.014.2290</li><li>office@willowcrest.com</li><li>web@willowcrest.com</li><li>12 Orchard Lane, Fairhaven</li></ul>
  <div class="watermark" style="left:98px;top:208px;width:172px;height:172px"></div>
  <div class="footer-rule" style="bottom:5px"></div>
  <div class="footer-rule gold" style="bottom:0"></div>
</section>

<!-- Business card front, light -->
<section class="sheet card" style="left:828px;top:50px;width:336px;height:196px">
  <div class="watermark" style="left:16px;top:30px;width:110px;height:110px"></div>
  <div class="card-name" style="left:156px;top:22px">Marcus Hale</div>
  <div class="card-role" style="left:157px;top:42px">Managing Director</div>
  <ul class="card-contacts" style="left:156px;top:86px"><li>0555.014.2290</li><li>0555.014.2291</li><li>0555.014.2292</li><li>office@willowcrest.com</li><li>web@willowcrest.com</li><li>12 Orchard Lane, Fairhaven, NM 87001</li></ul>
  <svg class="wave bottom" viewBox="0 0 336 42" height="42" preserveAspectRatio="none">
    <path d="M0 14C80 2 160 8 230 22C280 30 310 20 336 10V42H0Z" fill="var(--gold)"/>
    <path d="M0 4C80 -4 160 4 230 18C280 26 310 18 336 6C310 22 280 32 230 26C160 14 80 6 0 12Z" fill="var(--ink)"/>
  </svg>
</section>

<!-- Business card back, light -->
<section class="sheet card" style="left:828px;top:284px;width:336px;height:196px">
  <div class="brand" style="left:30px;top:74px;gap:8px"><span class="brand-dot" style="width:34px;height:34px"></span><span class="brand-name" style="font-size:17px">Willowcrest Trial<br>Desk</span></div>
  <svg class="wave bottom" viewBox="0 0 336 42" height="42" preserveAspectRatio="none">
    <path d="M0 14C80 2 160 8 230 22C280 30 310 20 336 10V42H0Z" fill="var(--gold)"/>
    <path d="M0 4C80 -4 160 4 230 18C280 26 310 18 336 6C310 22 280 32 230 26C160 14 80 6 0 12Z" fill="var(--ink)"/>
  </svg>
</section>

<!-- Business card front, dark -->
<section class="sheet card dark" style="left:828px;top:532px;width:336px;height:196px">
  <div class="watermark" style="left:16px;top:28px;width:126px;height:126px"></div>
  <div class="card-name" style="left:156px;top:22px">Marcus Hale</div>
  <div class="card-role" style="left:157px;top:42px">Managing Director</div>
  <ul class="card-contacts" style="left:156px;top:104px"><li>+0 555.014.2290</li><li>+0 555.014.2291</li><li>+0 555.014.2292</li><li>office@willowcrest.com</li><li>web@willowcrest.com</li><li>12 Orchard Lane, Fairhaven, NM 87001</li></ul>
</section>

<!-- Business card back, dark -->
<section class="sheet card dark" style="left:828px;top:744px;width:336px;height:196px">
  <div class="brand" style="left:30px;top:82px;gap:8px"><span class="brand-dot" style="width:34px;height:34px"></span><span class="brand-name" style="font-size:17px">Willowcrest Trial<br>Desk</span></div>
</section>

<!-- Envelope front A -->
<section class="sheet envelope" style="left:28px;top:578px;width:383px;height:174px">
  <svg class="wave top" viewBox="0 0 383 34" height="34" preserveAspectRatio="none">
    <path d="M0 0H383V20C310 28 240 6 160 10C95 13 40 18 0 16Z" fill="var(--gold)"/>
    <path d="M0 18C40 20 95 15 160 12C240 8 310 30 383 22C310 34 240 16 160 18C95 21 40 28 0 28Z" fill="var(--ink)"/>
  </svg>
  <div class="brand" style="left:20px;top:44px"><span class="brand-dot" style="width:20px;height:20px"></span><span class="brand-name" style="font-size:9px">Willowcrest Trial<br>Desk</span></div>
  <ul class="contacts" style="left:48px;top:72px"><li>0555.014.2290</li><li>office@willowcrest.com</li><li>web@willowcrest.com</li><li>12 Orchard Lane, Fairhaven, NM 87001</li></ul>
  <div class="watermark" style="left:200px;top:26px;width:100px;height:100px"></div>
  <div class="footer-rule" style="bottom:5px"></div>
  <div class="footer-rule gold" style="bottom:0"></div>
</section>

<!-- Envelope front B -->
<section class="sheet envelope" style="left:28px;top:772px;width:383px;height:176px">
  <svg class="wave top" viewBox="0 0 383 34" height="34" preserveAspectRatio="none">
    <path d="M0 0H383V20C310 28 240 6 160 10C95 13 40 18 0 16Z" fill="var(--gold)"/>
    <path d="M0 18C40 20 95 15 160 12C240 8 310 30 383 22C310 34 240 16 160 18C95 21 40 28 0 28Z" fill="var(--ink)"/>
  </svg>
  <div class="brand" style="left:20px;top:44px"><span class="brand-dot" style="width:20px;height:20px"></span><span class="brand-name" style="font-size:9px">Willowcrest Trial<br>Desk</span></div>
  <ul class="contacts" style="left:48px;top:68px"><li style="gap:0">12 Orchard Lane, Fairhaven, NM 87001</li></ul>
  <div class="watermark" style="left:200px;top:26px;width:100px;height:100px"></div>
  <ul class="contacts" style="left:20px;top:158px;display:flex;gap:14px"><li>0555.014.2290</li><li>office@willowcrest.com</li><li>web@willowcrest.com</li></ul>
  <div class="footer-rule" style="bottom:5px"></div>
  <div class="footer-rule gold" style="bottom:0"></div>
</section>

<!-- Envelope back -->
<section class="sheet envelope" style="left:433px;top:773px;width:383px;height:175px">
  <div class="flap"><span class="flap-dot"></span></div>
</section>

<div class="options">Letterhead 2 options<br>Envelope 2 front 1 back options<br>Business card 2 front 2back options</div>

</body>
</html>
```